Senior sex novelty store providing a private method for acquiring the products and knowledge

Our business supplies novelty sex products and services, specializing in the 50+ demographic. Products include sex products for individuals and couples. Services include webinars and teleseminars that address various sex and relationship issues. We are dedicated to providing discreet delivery of products and knowledge to people over 50 entering a new phase of life, facing new challenges. Our entire process from site through shipping is kept private to allow our customers the freedom to shop and learn in the privacy of their own home.

Target Market(s)

Seniors over 50 years old

Industry/Entity Type

Store

Number of Pages Required

1 page

Font styles to use
Serif

Requirements
Must have
• place for business description with a private look
Should not have
• anything sleazy

```html
<!DOCTYPE html>
<html lang="en">
<head>
<meta charset="utf-8">
<title>Your Company – Private Store</title>
<link rel="stylesheet" href="https://fonts.googleapis.com/css2?family=Cinzel:wght@400;700&family=PT+Sans:wght@400;700&display=swap">
<style>
:root{
  --red:#c8202a;
  --red-dark:#a81820;
  --header:#2d2928;
  --panel:#3b3736;
  --panel-line:#454140;
  --card:#ffffff;
  --card-img:#e9e7e8;
  --blog-bg:#eeeef2;
  --text-dark:#2a2a2a;
  --text-mid:#555;
  --subscribe:#1c1d26;
  --footer:#141414;
  --white:#ffffff;
  --muted:#c9c6c4;
}
*{box-sizing:border-box;margin:0;padding:0}
html,body{width:1200px;height:3506px;overflow:hidden}
body{font-family:"PT Sans",Arial,sans-serif;background:var(--header);color:var(--white);position:relative}
.serif{font-family:"Cinzel",Georgia,serif}

/* header */
.site-header{position:absolute;left:0;top:0;width:1200px;height:352px;background:var(--header)}
.account{position:absolute;right:108px;top:50px;font-size:12px;letter-spacing:.5px;color:var(--muted);display:flex;gap:20px;align-items:center}
.account .cart{display:flex;gap:6px;align-items:center}
.brand{position:absolute;left:0;top:60px;width:1200px;text-align:center}
.brand-mark{display:block;margin:0 auto 14px;width:40px;height:40px;border:3px solid var(--white)}
.brand-name{font-family:"Cinzel",Georgia,serif;font-size:46px;line-height:1;letter-spacing:1px}
.brand-tag{font-family:"Cinzel",Georgia,serif;font-size:30px;line-height:1;margin-top:6px}
.brand-rule{width:150px;height:3px;background:var(--red);margin:16px auto 0}
.main-nav{position:absolute;left:0;top:298px;width:1200px;display:flex;justify-content:center;align-items:center;gap:26px;font-size:17px}
.main-nav a{color:var(--white);text-decoration:none}
.main-nav a.active{font-weight:700}
.main-nav .dot{width:6px;height:6px;border-radius:50%;background:var(--white)}

/* hero */
.hero{position:absolute;left:0;top:352px;width:1200px;height:526px;background:linear-gradient(100deg,#6f5a52 0%,#c9b4a7 35%,#eadfd6 65%,#d8c7b8 100%)}

/* search */
.search-bar{position:absolute;left:0;top:878px;width:1200px;height:73px;background:var(--red);display:flex;align-items:center;padding-left:108px}
.search-label{font-size:18px;letter-spacing:1px;width:214px}
.search-field{height:36px;background:var(--white);color:#888;font-size:13px;display:flex;align-items:center;padding-left:12px;gap:6px;margin-right:16px}
.search-btn{height:32px;width:98px;background:#444;color:var(--white);font-size:14px;display:flex;align-items:center;justify-content:center}

/* store */
.store{position:absolute;left:0;top:951px;width:1200px;height:1338px;background:var(--panel)}
.store-title{position:absolute;top:106px;width:1200px;text-align:center;font-size:30px}
.store-intro{position:absolute;top:152px;left:330px;width:540px;text-align:center;font-size:15px;line-height:1.45;color:var(--muted)}
.card{position:absolute;width:322px;height:398px;background:var(--card);color:var(--text-dark);text-align:center}
.card-img{height:214px;background:var(--card-img)}
.card-badge{position:absolute;left:14px;top:12px;background:var(--red);color:var(--white);font-size:11px;padding:8px 12px}
.card-title{font-family:"Cinzel",Georgia,serif;font-size:21px;margin-top:26px}
.card-rule{width:56px;height:3px;background:var(--red);margin:8px auto 0}
.card-actions{display:flex;justify-content:center;gap:34px;margin-top:36px}
.icon-btn{width:44px;height:44px;border-radius:50%;background:var(--red);display:flex;align-items:center;justify-content:center}
.see-more{position:absolute;top:1230px;width:1200px;text-align:center;font-size:18px;letter-spacing:2px;font-family:"Cinzel",Georgia,serif}

/* blog */
.blog{position:absolute;left:0;top:2289px;width:1200px;height:609px;background:linear-gradient(90deg,#f2f2f5 0%,#e9e8ec 60%,#c9c3c6 100%);color:var(--text-dark)}
.blog-title{position:absolute;top:112px;width:1200px;text-align:center;font-size:31px}
.post{position:absolute;top:222px;width:460px}
.post h3{font-size:16px;font-weight:400;line-height:1.35;text-transform:uppercase}
.post time{display:block;color:var(--red);font-size:14px;margin-top:24px}
.post p{font-size:13px;line-height:1.5;color:var(--text-mid);margin-top:16px}
.post .read-more{display:block;color:var(--red);font-size:13px;margin-top:44px}
.social{position:absolute;left:0;top:2882px;width:1200px;display:flex;justify-content:center;gap:10px;z-index:2}
.social span{width:42px;height:42px;border-radius:50%}

/* subscribe */
.subscribe{position:absolute;left:0;top:2898px;width:1200px;height:518px;background:linear-gradient(90deg,#16171f 0%,#2a2428 55%,#1b1c24 100%);text-align:center}
.subscribe-title{position:absolute;top:80px;width:1200px;font-size:20px;letter-spacing:2px;font-family:"Cinzel",Georgia,serif}
.subscribe-text{position:absolute;top:126px;width:1200px;font-size:16px;color:var(--muted)}
.subscribe-form{position:absolute;left:246px;top:185px;width:708px;height:42px;display:flex}
.subscribe-input{flex:1;background:var(--white)}
.subscribe-btn{width:84px;background:var(--red);font-size:13px;display:flex;align-items:center;justify-content:center}
.stats{position:absolute;left:168px;top:350px;width:864px;display:flex}
.stat{flex:1;border-left:2px solid #6a6670;padding:6px 0}
.stat:first-child{border-left:none}
.stat strong{display:block;font-family:"Cinzel",Georgia,serif;font-weight:400;font-size:26px}
.stat span{font-size:15px;color:var(--muted)}

/* footer */
.site-footer{position:absolute;left:0;top:3416px;width:1200px;height:90px;background:var(--footer);font-size:14px;color:var(--muted)}
.copyright{position:absolute;left:94px;top:38px}
.copyright b{color:var(--red);font-weight:400}
.footer-links{position:absolute;right:94px;top:38px;display:flex;gap:28px}
</style>
</head>
<body>

<header class="site-header">
  <div class="account">
    <span>LOGIN / SIGNUP</span>
    <span class="cart">
      <svg width="16" height="14" viewBox="0 0 16 14"><path d="M1 1h3l2 8h8l2-6H5" fill="none" stroke="#c8202a" stroke-width="2"/><circle cx="7" cy="12" r="1.5" fill="#c8202a"/><circle cx="13" cy="12" r="1.5" fill="#c8202a"/></svg>
      $ 130.00
    </span>
  </div>
  <div class="brand">
    <span class="brand-mark"></span>
    <div class="brand-name">YOUR LOGO HERE</div>
    <div class="brand-tag">TAG LINE GOES HERE</div>
    <div class="brand-rule"></div>
  </div>
  <nav class="main-nav">
    <a class="active" href="#">HOMEPAGE</a><span class="dot"></span>
    <a href="#">PRODUCTS</a><span class="dot"></span>
    <a href="#">SERVICES</a><span class="dot"></span>
    <a href="#">SHIPPING</a><span class="dot"></span>
    <a href="#">PAYMENT</a><span class="dot"></span>
    <a href="#">HELP</a><span class="dot"></span>
    <a href="#">CONTACT</a>
  </nav>
</header>

<div class="hero" role="img" aria-label="Hero photograph of a woman in lingerie resting on soft cream bedding"></div>

<form class="search-bar">
  <span class="search-label">SEARCH PRODUCTS</span>
  <span class="search-field" style="width:268px">
    <svg width="10" height="10" viewBox="0 0 10 10"><path d="M1 9l6-6 2 2-6 6H1z" fill="#555"/></svg>
  </span>
  <span class="search-field" style="width:178px">
    <svg width="10" height="10" viewBox="0 0 10 10"><rect x="1" y="1" width="8" height="8" fill="#555"/></svg>Categories
  </span>
  <span class="search-field" style="width:178px">
    <svg width="10" height="12" viewBox="0 0 10 12"><path d="M5 11C2 7 1 5.5 1 4a4 4 0 0 1 8 0c0 1.5-1 3-4 7z" fill="#555"/></svg>Locations
  </span>
  <span class="search-btn">Search</span>
</form>

<main class="store">
  <h2 class="store-title serif">WELCOME TO OUR STORE</h2>
  <p class="store-intro">FLorem ipsum dolor sit amet voluptatem fugit aut illo omnis explicabo ipsa nemo rem ipsam quasi illo dolores ut voluptatem doloremque perspiciatis beatae magni architecto</p>

  <article class="card" style="left:94px;top:272px">
    <div class="card-img" role="img" aria-label="Product photo: pink curved personal massager"></div>
    <span class="card-badge">102 items</span>
    <h3 class="card-title">NEW ARRIVALS</h3><div class="card-rule"></div>
    <div class="card-actions">
      <span class="icon-btn"><svg width="18" height="18" viewBox="0 0 18 18"><circle cx="7.5" cy="7.5" r="5" fill="none" stroke="#fff" stroke-width="2"/><path d="M11 11l5 5M5.5 7.5h4M7.5 5.5v4" stroke="#fff" stroke-width="2"/></svg></span>
      <span class="icon-btn"><svg width="14" height="18" viewBox="0 0 14 18"><path d="M7 17C2.5 11 1 8.5 1 6.5a6 6 0 0 1 12 0c0 2-1.5 4.5-6 10.5z" fill="#fff"/><circle cx="7" cy="6.5" r="2.2" fill="#c8202a"/></svg></span>
      <span class="icon-btn"><svg width="16" height="16" viewBox="0 0 16 16" fill="#fff"><circle cx="2.5" cy="2.5" r="2"/><circle cx="8" cy="2.5" r="2"/><circle cx="13.5" cy="2.5" r="2"/><circle cx="2.5" cy="8" r="2"/><circle cx="8" cy="8" r="2"/><circle cx="13.5" cy="8" r="2"/><circle cx="2.5" cy="13.5" r="2"/><circle cx="8" cy="13.5" r="2"/><circle cx="13.5" cy="13.5" r="2"/></svg></span>
    </div>
  </article>

  <article class="card" style="left:439px;top:272px">
    <div class="card-img" role="img" aria-label="Product photo: pink ribbed wand held in a hand" style="background:#e7d7df"></div>
    <span class="card-badge">126 items</span>
    <h3 class="card-title">TOP PRODUCTS</h3><div class="card-rule"></div>
    <div class="card-actions">
      <span class="icon-btn"><svg width="18" height="18" viewBox="0 0 18 18"><circle cx="7.5" cy="7.5" r="5" fill="none" stroke="#fff" stroke-width="2"/><path d="M11 11l5 5M5.5 7.5h4M7.5 5.5v4" stroke="#fff" stroke-width="2"/></svg></span>
      <span class="icon-btn"><svg width="14" height="18" viewBox="0 0 14 18"><path d="M7 17C2.5 11 1 8.5 1 6.5a6 6 0 0 1 12 0c0 2-1.5 4.5-6 10.5z" fill="#fff"/><circle cx="7" cy="6.5" r="2.2" fill="#c8202a"/></svg></span>
      <span class="icon-btn"><svg width="16" height="16" viewBox="0 0 16 16" fill="#fff"><circle cx="2.5" cy="2.5" r="2"/><circle cx="8" cy="2.5" r="2"/><circle cx="13.5" cy="2.5" r="2"/><circle cx="2.5" cy="8" r="2"/><circle cx="8" cy="8" r="2"/><circle cx="13.5" cy="8" r="2"/><circle cx="2.5" cy="13.5" r="2"/><circle cx="8" cy="13.5" r="2"/><circle cx="13.5" cy="13.5" r="2"/></svg></span>
    </div>
  </article>

  <article class="card" style="left:784px;top:272px">
    <div class="card-img" role="img" aria-label="Product photo: peach-toned soft body product" style="background:#ececec"></div>
    <span class="card-badge">312 items</span>
    <h3 class="card-title">PROMOS</h3><div class="card-rule"></div>
    <div class="card-actions">
      <span class="icon-btn"><svg width="18" height="18" viewBox="0 0 18 18"><circle cx="7.5" cy="7.5" r="5" fill="none" stroke="#fff" stroke-width="2"/><path d="M11 11l5 5M5.5 7.5h4M7.5 5.5v4" stroke="#fff" stroke-width="2"/></svg></span>
      <span class="icon-btn"><svg width="14" height="18" viewBox="0 0 14 18"><path d="M7 17C2.5 11 1 8.5 1 6.5a6 6 0 0 1 12 0c0 2-1.5 4.5-6 10.5z" fill="#fff"/><circle cx="7" cy="6.5" r="2.2" fill="#c8202a"/></svg></span>
      <span class="icon-btn"><svg width="16" height="16" viewBox="0 0 16 16" fill="#fff"><circle cx="2.5" cy="2.5" r="2"/><circle cx="8" cy="2.5" r="2"/><circle cx="13.5" cy="2.5" r="2"/><circle cx="2.5" cy="8" r="2"/><circle cx="8" cy="8" r="2"/><circle cx="13.5" cy="8" r="2"/><circle cx="2.5" cy="13.5" r="2"/><circle cx="8" cy="13.5" r="2"/><circle cx="13.5" cy="13.5" r="2"/></svg></span>
    </div>
  </article>

  <article class="card" style="left:94px;top:749px">
    <div class="card-img" role="img" aria-label="Product photo: textured finger sleeve on a hand" style="background:#ebe3df"></div>
    <span class="card-badge">102 items</span>
    <h3 class="card-title">FOR INDIVIDUALS</h3><div class="card-rule"></div>
    <div class="card-actions">
      <span class="icon-btn"><svg width="18" height="18" viewBox="0 0 18 18"><circle cx="7.5" cy="7.5" r="5" fill="none" stroke="#fff" stroke-width="2"/><path d="M11 11l5 5M5.5 7.5h4M7.5 5.5v4" stroke="#fff" stroke-width="2"/></svg></span>
      <span class="icon-btn"><svg width="14" height="18" viewBox="0 0 14 18"><path d="M7 17C2.5 11 1 8.5 1 6.5a6 6 0 0 1 12 0c0 2-1.5 4.5-6 10.5z" fill="#fff"/><circle cx="7" cy="6.5" r="2.2" fill="#c8202a"/></svg></span>
      <span class="icon-btn"><svg width="16" height="16" viewBox="0 0 16 16" fill="#fff"><circle cx="2.5" cy="2.5" r="2"/><circle cx="8" cy="2.5" r="2"/><circle cx="13.5" cy="2.5" r="2"/><circle cx="2.5" cy="8" r="2"/><circle cx="8" cy="8" r="2"/><circle cx="13.5" cy="8" r="2"/><circle cx="2.5" cy="13.5" r="2"/><circle cx="8" cy="13.5" r="2"/><circle cx="13.5" cy="13.5" r="2"/></svg></span>
    </div>
  </article>

  <article class="card" style="left:439px;top:749px">
    <div class="card-img" role="img" aria-label="Product photo: pink padded cuffs with a chain" style="background:#dcdde6"></div>
    <span class="card-badge">126 items</span>
    <h3 class="card-title">FOR COUPLES</h3><div class="card-rule"></div>
    <div class="card-actions">
      <span class="icon-btn"><svg width="18" height="18" viewBox="0 0 18 18"><circle cx="7.5" cy="7.5" r="5" fill="none" stroke="#fff" stroke-width="2"/><path d="M11 11l5 5M5.5 7.5h4M7.5 5.5v4" stroke="#fff" stroke-width="2"/></svg></span>
      <span class="icon-btn"><svg width="14" height="18" viewBox="0 0 14 18"><path d="M7 17C2.5 11 1 8.5 1 6.5a6 6 0 0 1 12 0c0 2-1.5 4.5-6 10.5z" fill="#fff"/><circle cx="7" cy="6.5" r="2.2" fill="#c8202a"/></svg></span>
      <span class="icon-btn"><svg width="16" height="16" viewBox="0 0 16 16" fill="#fff"><circle cx="2.5" cy="2.5" r="2"/><circle cx="8" cy="2.5" r="2"/><circle cx="13.5" cy="2.5" r="2"/><circle cx="2.5" cy="8" r="2"/><circle cx="8" cy="8" r="2"/><circle cx="13.5" cy="8" r="2"/><circle cx="2.5" cy="13.5" r="2"/><circle cx="8" cy="13.5" r="2"/><circle cx="13.5" cy="13.5" r="2"/></svg></span>
    </div>
  </article>

  <article class="card" style="left:784px;top:749px">
    <div class="card-img" role="img" aria-label="Product photo: purple curved couples massager" style="background:#f2f2f2"></div>
    <span class="card-badge">312 items</span>
    <h3 class="card-title">OTHER PRODUCTS</h3><div class="card-rule"></div>
    <div class="card-actions">
      <span class="icon-btn"><svg width="18" height="18" viewBox="0 0 18 18"><circle cx="7.5" cy="7.5" r="5" fill="none" stroke="#fff" stroke-width="2"/><path d="M11 11l5 5M5.5 7.5h4M7.5 5.5v4" stroke="#fff" stroke-width="2"/></svg></span>
      <span class="icon-btn"><svg width="14" height="18" viewBox="0 0 14 18"><path d="M7 17C2.5 11 1 8.5 1 6.5a6 6 0 0 1 12 0c0 2-1.5 4.5-6 10.5z" fill="#fff"/><circle cx="7" cy="6.5" r="2.2" fill="#c8202a"/></svg></span>
      <span class="icon-btn"><svg width="16" height="16" viewBox="0 0 16 16" fill="#fff"><circle cx="2.5" cy="2.5" r="2"/><circle cx="8" cy="2.5" r="2"/><circle cx="13.5" cy="2.5" r="2"/><circle cx="2.5" cy="8" r="2"/><circle cx="8" cy="8" r="2"/><circle cx="13.5" cy="8" r="2"/><circle cx="2.5" cy="13.5" r="2"/><circle cx="8" cy="13.5" r="2"/><circle cx="13.5" cy="13.5" r="2"/></svg></span>
    </div>
  </article>

  <div class="see-more">SEE MORE PRODUCTS</div>
</main>

<section class="blog" role="img" aria-label="Faded background photograph of an embracing couple">
  <h2 class="blog-title serif">RECENT NEWS FROM BLOG</h2>
  <article class="post" style="left:94px">
    <h3>Omnis aut aperiam ab ipsam ipsa odit aut aperiam aut aspernatur veritatis unde</h3>
    <time>April 28, 2015</time>
    <p>Lorem ipsum dolor sit amet voluptatem fugit aut illo omnisup explicabo nemo rem ipsam quasi illo dolores voluptatem doloremque perspiciatis magni architecto odit odit, aspernatur magni quae aperiam aut veritatis eos aut volupte doloremque perspiciati error natus illo natus inventore aut quasi consequuntur consequuntur ipsa odit aspernatur iste sit quae explicabo dicta quasi..</p>
    <span class="read-more">READ MORE</span>
  </article>
  <article class="post" style="left:650px">
    <h3>Ipsam ipsa odit aut aperiam aut aspernatur veritatis unde omnis aut aperiam ab</h3>
    <time>April 28, 2015</time>
    <p>Lorem ipsum dolor sit amet voluptatem fugit aut illo omnisup explicabo nemo rem ipsam quasi illo dolores voluptatem doloremque perspiciatis magni architecto odit odit, aspernatur magni quae aperiam aut veritatis eos aut volupte doloremque perspiciati error natus illo natus inventore aut quasi consequuntur consequuntur ipsa odit aspernatur iste sit quae explicabo dicta quasi..</p>
    <span class="read-more">READ MORE</span>
  </article>
</section>

<div class="social" aria-label="Social links">
  <span style="background:#3b5998"></span>
  <span style="background:#1da1f2"></span>
  <span style="background:#cb2027"></span>
  <span style="background:#dd4b39"></span>
</div>

<section class="subscribe" role="img" aria-label="Dark background photograph of a couple close together">
  <h2 class="subscribe-title">PLEASE SUBSCRIBE</h2>
  <p class="subscribe-text">Get our newsletter for various sex new release, promo of the month and relationship issues</p>
  <div class="subscribe-form"><span class="subscribe-input"></span><span class="subscribe-btn">Subscribe</span></div>
  <div class="stats">
    <div class="stat"><strong>180 MILLION</strong><span>Products</span></div>
    <div class="stat"><strong>860 MILLION</strong><span>Members</span></div>
    <div class="stat"><strong>250 MILLION</strong><span>Problem Solved</span></div>
    <div class="stat"><strong>109 MILLION</strong><span>Followers</span></div>
  </div>
</section>

<footer class="site-footer">
  <span class="copyright">© 2015 <b>YOUR COMPANY</b></span>
  <nav class="footer-links">
    <span>About us</span><span>Privacy policy</span><span>Terms and use</span><span>Countries</span><span>FAQ</span><span>Contact</span>
  </nav>
</footer>

</body>
</html>
```